Quite your look: needs a logo design and a business card

The business name is called: Quite your look. It's all about fashion for everyone who needs to gain confidence and find his own style: Image Consultant, Personal Shopper. Here my Facebook fan page: https://www.examplebook.test/pages/Quite-your-look/804213967520431

I would like a smart logo & business card. The design has to be smart and long lasting. I like simplicity ("less is more"). The image needs to bring over seriousness and style. I target people from 35-65 years old. I would love to have smart warm colours like brown mole or anthracite, eventually with some berry or bordeaux red.

The copy is the following:
Quite your look
Daphne Volkers
Mobile: +27 71 436 02 59
eMail: volkers.daphne@mailbox.test
Cape Town

Target Market(s)

Core target group: 35-65 years old women; wealthy; living in Cape Town
Larger target group: South Africa; eventually men too

Industry/Entity Type

Business

```html
<!DOCTYPE html>
<html lang="en">
<head>
<meta charset="utf-8">
<title>Quite your look – Daphne Volkers</title>
<link rel="stylesheet" href="https://fonts.googleapis.com/css2?family=Sorts+Mill+Goudy:ital@0;1&display=swap">
<style>
  :root {
    --bordeaux: #8b3c46;
    --bordeaux-light: #94464f;
    --bordeaux-deep: #823741;
    --brand-brown: #3a1519;
    --frame: #2a2a2a;
    --ink-white: #ffffff;
    --band-blue: #d2e2f3;
    --ink-dark: #1c1c1c;
  }
  html, body {
    margin: 0;
    padding: 0;
    width: 728px;
    height: 1200px;
    overflow: hidden;
    background: #ffffff;
  }
  .card {
    position: relative;
    width: 728px;
    height: 1200px;
    box-sizing: border-box;
    border: 3px solid var(--frame);
    background: var(--bordeaux);
    overflow: hidden;
    font-family: "Sorts Mill Goudy", Georgia, serif;
  }
  .fashion-backdrop {
    position: absolute;
    inset: 0;
    background: radial-gradient(ellipse at 50% 45%, var(--bordeaux-light) 0%, var(--bordeaux) 60%, var(--bordeaux-deep) 100%);
  }
  .brand-name {
    position: absolute;
    left: 367px;
    top: 262px;
    margin: 0;
    transform: translate(-50%, -50%) rotate(-30deg);
    white-space: nowrap;
    font-size: 104px;
    font-weight: 400;
    color: var(--brand-brown);
    line-height: 1;
  }
  .stylist {
    position: absolute;
    left: 0;
    right: 0;
    top: 612px;
    text-align: center;
    color: var(--ink-white);
  }
  .stylist-name {
    margin: 0;
    font-size: 46px;
    font-weight: 400;
    font-variant: small-caps;
    letter-spacing: 0.5px;
    line-height: 1;
  }
  .stylist-role {
    margin: 12px 0 0;
    font-size: 32px;
    font-style: italic;
    line-height: 1;
  }
  .contact-band {
    position: absolute;
    left: 0;
    right: 0;
    top: 975px;
    height: 150px;
    background: var(--band-blue);
    color: var(--ink-dark);
    display: flex;
    flex-direction: column;
    align-items: center;
    justify-content: center;
    gap: 14px;
    font-size: 35px;
  }
  .contact-line {
    display: flex;
    align-items: center;
    gap: 10px;
    margin: 0;
    line-height: 1;
    white-space: nowrap;
  }
  .contact-icon {
    width: 44px;
    height: 44px;
    flex: none;
  }
</style>
</head>
<body>
  <main class="card">
    <div class="fashion-backdrop" role="img" aria-label="Faint line-drawn pattern of clothes, shoes, handbags and accessories"></div>

    <h1 class="brand-name">Quite your look</h1>

    <section class="stylist">
      <p class="stylist-name">Daphne Volkers</p>
      <p class="stylist-role">Personal Stylist</p>
    </section>

    <section class="contact-band">
      <p class="contact-line">
        <svg class="contact-icon" viewBox="0 0 44 44" aria-hidden="true">
          <circle cx="22" cy="22" r="19" fill="none" stroke="#1c1c1c" stroke-width="2.5"/>
          <path d="M15 12 c-3 2 -3 6 -1 11 c2 5 6 9 10 10 c3 1 5 0 6 -2 l-4 -4 c-1 1 -2 2 -3 1 c-2 -1 -5 -5 -5 -7 c0 -1 1 -2 2 -2 z" fill="#1c1c1c"/>
        </svg>
        <span>+27 71 436 02 59 - Cape Town -</span>
      </p>
      <p class="contact-line">
        <svg class="contact-icon" viewBox="0 0 44 44" aria-hidden="true">
          <rect x="3" y="9" width="38" height="26" fill="none" stroke="#1c1c1c" stroke-width="2.5"/>
          <path d="M3 9 L22 25 L41 9 M3 35 L17 21 M41 35 L27 21" fill="none" stroke="#1c1c1c" stroke-width="2.5"/>
        </svg>
        <span>volkers.daphne@mailbox.test</span>
      </p>
    </section>
  </main>
</body>
</html>
```